Stationary & Business Card for a Rock climbing company based primarily in Joshua Tree NP
Use provided logo
Stationary & Business Card for a Rock climbing company based primarily in Joshua Tree NP - Outdoors
Creative Brief
Simple
Garrick Fenn
Director
27615 Marrow Lane Victorville, CA 92307
garrickfenn@mailbrook.com
www.ridgepathoutfitters.com

```html
<!DOCTYPE html>
<html lang="en">
<head>
<meta charset="utf-8">
<title>Ridgepath Outfitters – Business Card</title>
<link href="https://fonts.googleapis.com/css2?family=Open+Sans:wght@400;600;700&display=swap" rel="stylesheet">
<style>
  :root {
    --backdrop: #e7e4e0;
    --card-white: #ffffff;
    --earth-brown: #3a2c27;
    --trail-orange: #f0921f;
    --ink-white: #f4efe9;
    --logo-brown: #4a3329;
  }
  * { box-sizing: border-box; margin: 0; padding: 0; }
  html, body {
    width: 1200px;
    height: 900px;
    overflow: hidden;
    background: var(--backdrop);
    font-family: "Open Sans", Arial, sans-serif;
  }
  .stage {
    width: 1200px;
    height: 900px;
    display: flex;
    align-items: center;
    justify-content: center;
  }
  .business-card {
    position: relative;
    width: 980px;
    height: 560px;
    background: var(--card-white);
    overflow: hidden;
    box-shadow: 0 12px 30px rgba(0,0,0,0.18);
  }
  .card-bands {
    position: absolute;
    inset: 0;
  }
  .brand-mark {
    position: absolute;
    left: 52px;
    top: 52px;
    display: flex;
    align-items: center;
    gap: 18px;
  }
  .brand-dot {
    width: 64px;
    height: 64px;
    border-radius: 50%;
    background: var(--trail-orange);
  }
  .brand-name {
    font-weight: 700;
    font-size: 30px;
    color: var(--logo-brown);
    letter-spacing: 0.5px;
  }
  .name-tab {
    position: absolute;
    left: 610px;
    top: 212px;
    width: 370px;
    height: 80px;
    background: var(--trail-orange);
    border-radius: 10px 0 0 10px;
    padding: 12px 0 0 40px;
    color: #ffffff;
  }
  .person-name {
    font-weight: 700;
    font-size: 26px;
    line-height: 1.15;
  }
  .person-title {
    font-weight: 400;
    font-size: 16px;
    margin-top: 4px;
    padding-left: 28px;
  }
  .contact-list {
    position: absolute;
    left: 40px;
    top: 322px;
    list-style: none;
    color: var(--ink-white);
    font-size: 17px;
    line-height: 1.25;
  }
  .contact-item {
    display: flex;
    align-items: flex-start;
    gap: 10px;
    margin-bottom: 6px;
  }
  .contact-icon {
    flex: none;
    width: 20px;
    height: 20px;
    margin-top: 1px;
  }
  .address-lines span { display: block; }
</style>
</head>
<body>
<main class="stage">
  <article class="business-card">
    <svg class="card-bands" width="980" height="560" viewBox="0 0 980 560" aria-hidden="true">
      <polygon points="0,292 620,232 980,232 980,560 0,560" fill="var(--earth-brown)"/>
      <polygon points="0,280 620,220 620,232 0,292" fill="var(--trail-orange)"/>
    </svg>

    <div class="brand-mark">
      <div class="brand-dot"></div>
      <div class="brand-name">Ridgepath Outfitters</div>
    </div>

    <div class="name-tab">
      <div class="person-name">Garrick Fenn</div>
      <div class="person-title">Director</div>
    </div>

    <ul class="contact-list">
      <li class="contact-item">
        <svg class="contact-icon" viewBox="0 0 20 20" aria-hidden="true">
          <circle cx="10" cy="10" r="10" fill="#fff"/>
          <path d="M5 10 L10 5.5 L15 10 M6.5 9 V14.5 H13.5 V9" fill="none" stroke="var(--earth-brown)" stroke-width="1.6"/>
        </svg>
        <div class="address-lines"><span>27615 Marrow Lane</span><span>Victorville, CA 92307</span></div>
      </li>
      <li class="contact-item">
        <svg class="contact-icon" viewBox="0 0 20 20" aria-hidden="true">
          <circle cx="10" cy="10" r="10" fill="#fff"/>
          <path d="M6.5 5 L8.5 5 L9.3 7.8 L8 8.8 Q9.2 11.2 11.3 12.1 L12.3 10.8 L15 11.6 L15 13.6 Q11 14.6 8 11.8 Q5.3 9 6.5 5 Z" fill="var(--earth-brown)"/>
        </svg>
        <span>(760) 555-0148</span>
      </li>
      <li class="contact-item">
        <svg class="contact-icon" viewBox="0 0 20 20" aria-hidden="true">
          <circle cx="10" cy="10" r="10" fill="#fff"/>
          <rect x="7" y="4.5" width="6" height="11" rx="1.2" fill="none" stroke="var(--earth-brown)" stroke-width="1.5"/>
          <circle cx="10" cy="13.4" r="0.8" fill="var(--earth-brown)"/>
        </svg>
        <span>(760) 555-0172</span>
      </li>
      <li class="contact-item">
        <svg class="contact-icon" viewBox="0 0 20 20" aria-hidden="true">
          <circle cx="10" cy="10" r="10" fill="#fff"/>
          <rect x="5" y="6.5" width="10" height="7" fill="none" stroke="var(--earth-brown)" stroke-width="1.4"/>
          <path d="M5 6.5 L10 10.5 L15 6.5" fill="none" stroke="var(--earth-brown)" stroke-width="1.4"/>
        </svg>
        <span>garrickfenn@mailbrook.com</span>
      </li>
      <li class="contact-item">
        <svg class="contact-icon" viewBox="0 0 20 20" aria-hidden="true">
          <circle cx="10" cy="10" r="10" fill="#fff"/>
          <circle cx="10" cy="10" r="5" fill="none" stroke="var(--earth-brown)" stroke-width="1.3"/>
          <path d="M5 10 H15 M10 5 Q7 10 10 15 M10 5 Q13 10 10 15" fill="none" stroke="var(--earth-brown)" stroke-width="1.1"/>
        </svg>
        <span>www.ridgepathoutfitters.com</span>
      </li>
    </ul>
  </article>
</main>
</body>
</html>
```